Business Card Design

We are a non profit organization that holds 10 days of races and car shows to raise money for autism. We stage the largest vintage race event in the country and the only one held on city streets.

We need business cards for myself and for 100 volunteers that stage the event. We like our cards to look exciting and to capture the essence of vintage racing.

Target Market(s)

sponsors and volunteers - most in the auto industry. This is not a TORVEX crowd

Industry/Entity Type

Non Profit

Contact Information for Business Card

Marcus Feldwright
Executive Director
Harborline Classic Motor Rally Association
2750 Kestrel Lane, Suite 214
Pittsburgh, PA 15907
feldwright@hcmra-example.org
cell 412 683-7142
www.hcmra-example.org

Font styles to use
Sans Serif

Colors
ec2027

Requirements
Must have
• our logo place a car image.Could place racing image on back of card along with website

Must include this statement small somewhere:
Benefitting the Brightpath Spectrum Society and Willowmere Ridge School

```html
<!DOCTYPE html>
<html lang="en">
<head>
<meta charset="utf-8">
<title>Business Card – Front and Back</title>
<link href="https://fonts.googleapis.com/css2?family=Open+Sans:wght@400;600;700&display=swap" rel="stylesheet">
<style>
  :root {
    --race-red: #d71f26;
    --card-charcoal: #2b2b2b;
    --card-white: #f4f4f4;
    --stage: #e6e6e6;
    --ink-light: #ffffff;
    --ink-dark: #2b2b2b;
    --rule: rgba(255,255,255,0.75);
  }
  * { box-sizing: border-box; margin: 0; padding: 0; }
  html, body {
    width: 1200px; height: 990px; overflow: hidden;
    background: var(--stage);
    font-family: "Open Sans", Arial, sans-serif;
  }
  .stage {
    width: 1200px; height: 990px;
    display: flex; justify-content: center; align-items: center; gap: 60px;
  }
  .card {
    width: 520px; height: 910px;
    position: relative;
    box-shadow: 0 6px 18px rgba(0,0,0,0.18);
  }
  /* Front */
  .card-front { background: var(--card-charcoal); }
  .brand-mark {
    position: absolute; top: 80px; left: 0; right: 0;
    display: flex; flex-direction: column; align-items: center; gap: 22px;
  }
  .brand-disc {
    width: 140px; height: 140px; border-radius: 50%;
    background: var(--race-red);
    border: 8px solid var(--ink-light);
  }
  .brand-name {
    color: var(--ink-light); font-weight: 700; font-size: 20px;
    letter-spacing: 2px; text-transform: uppercase; text-align: center;
    line-height: 1.4; max-width: 340px;
  }
  .contact-panel {
    position: absolute; left: 0; right: 0; bottom: 0; height: 530px;
    background: var(--race-red);
    padding: 46px 50px 30px;
    color: var(--ink-light);
    display: flex; flex-direction: column;
  }
  .holder-name {
    font-size: 32px; font-weight: 700; text-transform: uppercase; letter-spacing: 1px;
    text-align: right; line-height: 1.2;
  }
  .holder-role {
    font-size: 16px; font-weight: 400; text-transform: uppercase; letter-spacing: 2px;
    text-align: right; margin-top: 4px; margin-bottom: 28px;
  }
  .contact-list { list-style: none; }
  .contact-item {
    display: flex; align-items: center; gap: 18px;
    padding: 12px 0; border-top: 1px solid var(--rule);
    font-size: 16px; line-height: 1.4;
  }
  .contact-item svg { width: 22px; height: 22px; flex: none; }
  .contact-item.address { align-items: flex-start; }
  .benefit-note {
    margin-top: auto; padding-top: 12px; border-top: 1px solid var(--rule);
    font-size: 12px; line-height: 1.45; text-align: center; opacity: 0.95;
  }
  /* Back */
  .card-back {
    background: var(--card-white);
    border: 34px solid var(--race-red);
    display: flex; flex-direction: column; align-items: center;
    padding: 40px 36px;
  }
  .racing-image {
    width: 100%; flex: 1;
    background: linear-gradient(160deg, #8a8a8a 0%, #3a3a3a 60%, #7a1b1f 100%);
  }
  .back-web {
    margin-top: 28px; font-size: 22px; font-weight: 700; color: var(--ink-dark);
    letter-spacing: 1px;
  }
  .back-rule { width: 80px; height: 4px; background: var(--race-red); margin-top: 12px; }
</style>
</head>
<body>
<main class="stage">
  <section class="card card-front" aria-label="Card front">
    <div class="brand-mark">
      <div class="brand-disc"></div>
      <div class="brand-name">Harborline Classic Motor Rally Association</div>
    </div>
    <div class="contact-panel">
      <h1 class="holder-name">Marcus Feldwright</h1>
      <p class="holder-role">Executive Director</p>
      <ul class="contact-list">
        <li class="contact-item">
          <svg viewBox="0 0 24 24" fill="#fff"><path d="M6.6 10.8a15.2 15.2 0 0 0 6.6 6.6l2.2-2.2a1 1 0 0 1 1-.25 11.4 11.4 0 0 0 3.6.57 1 1 0 0 1 1 1V20a1 1 0 0 1-1 1A17 17 0 0 1 3 4a1 1 0 0 1 1-1h3.5a1 1 0 0 1 1 1c0 1.25.2 2.45.57 3.6a1 1 0 0 1-.25 1z"/></svg>
          cell 412 683-7142
        </li>
        <li class="contact-item">
          <svg viewBox="0 0 24 24" fill="#fff"><path d="M3 5h18v14H3z M4 6.5v.4l8 5.2 8-5.2v-.4z" fill-rule="evenodd"/></svg>
          feldwright@hcmra-example.org
        </li>
        <li class="contact-item">
          <svg viewBox="0 0 24 24" fill="none" stroke="#fff" stroke-width="1.8"><circle cx="12" cy="12" r="9"/><path d="M3 12h18M12 3c3 3.2 3 14.8 0 18M12 3c-3 3.2-3 14.8 0 18"/></svg>
          www.hcmra-example.org
        </li>
        <li class="contact-item address">
          <svg viewBox="0 0 24 24" fill="#fff"><path d="M12 2a7 7 0 0 0-7 7c0 5 7 13 7 13s7-8 7-13a7 7 0 0 0-7-7zm0 9.5A2.5 2.5 0 1 1 12 6.5a2.5 2.5 0 0 1 0 5z"/></svg>
          <span>2750 Kestrel Lane, Suite 214<br>Pittsburgh, PA 15907</span>
        </li>
      </ul>
      <p class="benefit-note">Benefitting the Brightpath Spectrum Society<br>and Willowmere Ridge School</p>
    </div>
  </section>
  <section class="card card-back" aria-label="Card back">
    <div class="racing-image" role="img" aria-label="Vintage race car on a city street circuit"></div>
    <p class="back-web">www.hcmra-example.org</p>
    <div class="back-rule"></div>
  </section>
</main>
</body>
</html>
```